Arizona Pool Company Brochure

**** UPDATE 2-8-2014 ****

Size should be 11" X 17" or larger (tri or bi fold).

We're going to let the contest run it's full duration to allow for more time spent on designs.

No black backgrounds.

Consideration should be given to having the text be easy to read and in a nice, organized format.

*****************************

We're looking for an eye-catching, colorful brochure that will explain what we do, who we are... and what sets us apart from the competition.

Our company provides swimming pool service, repair, and custom renovations throughout the Phoenix, Arizona metropolitan area. These brochures will be hand-delivered to each prospective customer we visit.

The brochure will include images of our work, product logos, and a unique design that separates our company apart from the rest.

The brochure should be tri-fold. Although, if a designer wants to (or has better ideas) for a different lay-out, then we're open to seeing what can be done.

Colors we like: Blue, White, Silver, Copper, Green (accent color)

We like designs that are unique/different. Professional. Creative. Sleek. Sexy. Custom. We don't want the brochure to be "pretentious". We'd like for these brochures to leave a lasting impression with our prospective clients... and hopefully earn us more business.

We don't want the brochure to be too wordy, however if the designer feels we need to cut back (or add), let us know.

Our motto is "Every Wave Stays Bright".

You can view some of our projects, and what we're about either at our website (tidewellaqua.com), Chatterbook (www.chatterbook/tidewellaqua), or Searchly+ (https://plus.google.com/+Tidewellaqua). Thank you!

- Print-

(Front) Logo

Service - Repair - Renovation
480-555-0147
tidewellaqua.com
service@tidewellaqua.com
Like Us On Chatterbook! Chatterbook LOGO
Searchly Circle LOGO

(Body) Why Choose Us?

Thank you for the opportunity for our company to become your pool service provider!

We’re committed to providing the best customer service possible! At the end of the day you want your pool to be clean, clear, operational, and for your service provider to be available when you need them!

We’re licensed with the Desert State Builders Licensing Office, Bonded, and Fully Insured.
A+ reviews with the Fair Trade Merchants Council, Marlo's Roster, Vetchly, Ornu, Chatterbook, and Searchly!
All technicians are employees... not sub-contractors! Our employees are hard working, dependable, professional, and expected to follow our strict protocol for servicing your pool.
Flat-fee service rates! Any additional equipment repairs, maintenance, or chemical implementations are directly authorized by you!
No contracts! Our Service Level Agreement Form allows you to select your desired level of authorization for equipment repairs, filter maintenance, and extra chemical implementation programs.
Our uniformed technicians arrive in distinctive, clean GPS-tracked company trucks.
We leave detailed service slips after each service visit. In addition, all service visit information is electronically recorded and stored.
Easy, online account management to view and pay invoices or authorize estimates.
Invoices, estimates, questions, pictures, and video are communicated via e-mail!
Free service calls to diagnose equipment issues outside of our normal service.
10% Service Client Discount for all repairs and replacement items.
Tidewell Aqua Service knows the importance of communication! We’re available by phone, email, or text all days of the week.

(Body) Our Methodology

We believe in 5 important factors in maintaining a clean, clear, and operational pool...

Good, Clean Water! Our local water supply contains high amounts of minerals. Pool chemicals add to this problem in a short amount of time. Our philosophy is to use the least amount of chemicals possible to achieve optimal water balance.
Efficient Water Flow! The invention of variable-speed pumps has enabled the ability to "dial in" proper water flow... while driving down energy costs.
Proper Filtration! Today’s high-capacity cartridge filters provide great filtration, save on wasted water from backwashing sand filters, and eliminate the need for water flow-restricting backwash valves.
Functioning Cleaning System! Having a working automatic cleaning system is vital in keeping the pool surface clean of debris and dirt... and free of staining.
A Dependable And Professional Pool Maintenance Technician! Our job is to not only oversee all of the items listed above... but to make sure your pool is in the best condition possible!

(Body) Equipment Repair & Installation

We’re educated on all phases of swimming pool equipment repair and installation... with a focus on energy-efficiency and optimum performance!

We’re an KVE & BTU Authorized Installer of variable-speed pool pumps. KVE & BTU trust us to properly install and calibrate all variable-speed pumps. We've been equipped to handle the new industry standards on variable-speed pumps since Arizona law went into effect January 1st, 2011.
We’re experts at acid washes and erasing the mineral build-up off of waterlines. All work is done in-house with our customized cleaning rig and trailer.
Heating systems. New efficiency standards have made installation and operation more affordable than ever.
Remote control automation systems. Technology now allows the user to easily view and control their entire pool system via a remote home computer, tablet, or phone!
Brilliant, color-changing LED lighting for pools and spas! The benefits of LED include brighter and broader displays... while lasting much longer than your typical light bulbs.
Salt systems provide a soft-water experience! In addition to the benefit of better feeling water, salt systems generate plenty of chlorine to keep your pool sanitized.

(Body) About Us

A native to Phoenix, Darren Whitcombe founded Tidewell Aqua Service in 2000. Our company was built from the ground up by way of hard work, word of mouth, and determination. Our company will always remain firmly grounded, and continue to develop systems that put our customers first!

Our philosophy is to treat every pool as if it were our own, run an efficient and organized business, and care for our employees.

Tidewell Aqua Service is a yearly, proud contributor to the Saguaro Youth Medical Center Splash Smart Day. Please educate and watch all children around water... every accident can be avoided.

(Back) Contact Us
Logos To Use, Files Uploaded: Marlo's Roster, FTMC, Quorvix, Searchly+, Chatterbook, KVE/BTU logo, Saguaro Youth Medical Center

Office: 480-555-0147 | Fax: 480-555-0193 | Email: service@tidewellaqua.com
tidewellaqua.com

Office / Warehouse Location
41762 East Kettle Lane, Suite 7
Phoenix, Arizona 85000
(NW of Kettle Lane & Mesquite Ridge Drive)

AZ ROC: 731402, 731403, 731404, 605218

Target Market(s)

We target a market of pool owners, which typically have more disposable income.

30 - 75 years old.

Our clients range from first-time home buyers, self-employed, business professionals, doctors, landlords, thousandaires, millionaires.

Industry/Entity Type

Pool Service

Font styles to use
Serif

Colors
0355a3
cfdfed
ffffff
3176b5
eaf1f7

Requirements
Must have
• Must use provided images. We've included a few pool pictures, and will let you decide which ones to incorporate throughout the brochure.

Logos Used:
Tidewell Aqua Service
Quorvix
FTMC
Marlo's Roster
KVE
BTU
Saguaro Youth Medical Center
Searchly+
Chatterbook

Image pic of some of our trucks.

Nice to have
• Equipment images worked in.
Should not have
• Cartoonish fonts or design. No "Love" hearts!!

```html
<!DOCTYPE html>
<html lang="en">
<head>
<meta charset="utf-8">
<title>Tidewell Aqua Service Brochure</title>
<link rel="stylesheet" href="https://fonts.googleapis.com/css2?family=Tinos:wght@400;700&family=Josefin+Sans:wght@300&display=swap">
<style>
  :root {
    --blue: #0355a3;
    --blue-mid: #3176b5;
    --navy: #14237a;
    --ice: #cfdfed;
    --mist: #eaf1f7;
    --white: #ffffff;
    --green: #8cc63f;
    --night-top: #6f63c9;
    --night-mid: #2c2440;
    --night-low: #0d1a3a;
    --pool-glow: #2a66c8;
  }
  * { margin: 0; padding: 0; box-sizing: border-box; }
  html, body { width: 1200px; height: 849px; overflow: hidden; background: var(--white); }
  .brochure {
    position: relative; width: 1200px; height: 849px; overflow: hidden;
    font-family: "Tinos", "Times New Roman", serif; color: var(--white);
  }
  .panel { position: absolute; top: 0; height: 849px; }
  .panel-contact, .panel-about {
    width: 300px;
    background: linear-gradient(180deg, var(--night-top) 0%, #c77a9a 22%, var(--night-mid) 36%, var(--night-low) 55%, var(--pool-glow) 70%, var(--night-low) 100%);
  }
  .panel-contact { left: 0; }
  .panel-about {
    left: 900px;
    background: linear-gradient(180deg, var(--night-top) 0%, #b86aa8 18%, var(--night-mid) 32%, #1c3f8a 60%, #102a5c 100%);
  }
  .panel-cover { left: 300px; width: 600px; background: var(--blue); }

  .heading { font-size: 15px; font-weight: 700; line-height: 18px; }
  .body-text { font-size: 14px; line-height: 16px; }
  .contact-block { position: absolute; left: 41px; width: 250px; }
  .contact-block strong { font-weight: 700; }

  .badges { position: absolute; left: 41px; top: 341px; }
  .badge { position: absolute; background: var(--white); border-radius: 4px; }
  .badge-tall { width: 52px; height: 84px; }
  .badge-wide { width: 86px; height: 62px; }

  .social { position: absolute; font-size: 11.5px; }
  .social-row { display: flex; align-items: center; gap: 12px; height: 24px; }
  .social-mark { width: 20px; height: 20px; background: var(--blue-mid); }
  .social-mark.alt { background: #d24a3a; }

  .about { position: absolute; left: 40px; top: 78px; width: 222px; font-size: 14.5px; line-height: 16.3px; }
  .about p { margin-top: 16px; }

  .cover-header { position: absolute; left: 0; top: 0; width: 600px; height: 78px; }
  .services {
    position: absolute; left: 48px; top: 8px; font-size: 27.5px; font-weight: 700; line-height: 29px; letter-spacing: 0.3px;
  }
  .hotline { position: absolute; right: 48px; top: 10px; text-align: right; font-weight: 700; }
  .hotline .phone { font-size: 20px; line-height: 22px; }
  .hotline .email { font-size: 15px; line-height: 18px; }

  .hero {
    position: absolute; left: 0; top: 78px; width: 600px; height: 484px;
    background: linear-gradient(160deg, #6f8f5a 0%, #a98a6a 22%, #6fb0b8 45%, #3f8fa0 70%, #2b6f7e 100%);
  }
  .motto {
    position: absolute; left: 270px; top: 426px; width: 300px; text-align: center;
    font-family: "Josefin Sans", "Helvetica", sans-serif; font-weight: 300;
    font-size: 32px; line-height: 50px; letter-spacing: 0.5px; text-transform: uppercase;
  }
  .divider { position: absolute; top: 562px; height: 12px; width: 300px; }
  .divider-blue { left: 0; background: var(--blue); }
  .divider-green { left: 300px; background: var(--green); }

  .cover-base { position: absolute; left: 0; top: 574px; width: 600px; height: 275px; }
  .brand { position: absolute; left: 0; top: 638px; width: 600px; display: flex; justify-content: center; align-items: center; gap: 10px; }
  .brand-dot { width: 34px; height: 34px; border-radius: 50%; background: var(--blue); }
  .brand-name { font-size: 38px; font-weight: 700; color: var(--blue); }
  .site { position: absolute; left: 0; top: 704px; width: 600px; text-align: center; font-size: 19px; color: var(--blue); }
</style>
</head>
<body>
<main class="brochure">

  <section class="panel panel-contact" role="img" aria-label="Evening sky over a lit backyard pool">
    <div class="contact-block" style="top:74px">
      <div class="heading">Contact Us</div>
      <div class="body-text">Office / Warehouse Location<br>41762 East Kettle Lane, Suite 7<br>Phoenix, Arizona 85000<br>(NW of Kettle Lane &amp;<br>Mesquite Ridge Drive)</div>
    </div>
    <div class="contact-block body-text" style="top:188px">
      <strong>Office</strong> 480-555-0147<br><strong>Fax</strong> 480-555-0193<br><strong>Email</strong> service@tidewellaqua.com
    </div>
    <div class="contact-block heading" style="top:253px">tidewellaqua.com</div>
    <div class="contact-block body-text" style="top:286px"><strong>AZ ROC</strong> 731402, 731403,<br>731404, 605218</div>

    <div class="badges" aria-label="Partner and listing badges">
      <div class="badge badge-tall" style="left:0;top:0"></div>
      <div class="badge badge-tall" style="left:65px;top:0"></div>
      <div class="badge badge-wide" style="left:0;top:97px"></div>
      <div class="badge badge-wide" style="left:98px;top:97px"></div>
      <div class="badge badge-wide" style="left:0;top:171px"></div>
    </div>

    <div class="social" style="left:41px;top:780px">
      <div class="social-row"><span class="social-mark"></span>www.chatterbook/tidewellaqua</div>
      <div class="social-row"><span class="social-mark alt"></span>circle.searchly.com/+Tidewellaqua</div>
    </div>
  </section>

  <section class="panel panel-cover">
    <svg class="cover-header" width="600" height="78" viewBox="0 0 600 78" aria-hidden="true">
      <rect width="600" height="78" fill="var(--blue)"/>
      <polygon points="0,0 348,0 302,78 0,78" fill="var(--green)"/>
    </svg>
    <div class="services">SERVICE • REPAIR<br>RENOVATION</div>
    <div class="hotline">
      <div class="phone">480-555-0147</div>
      <div class="email">service@tidewellaqua.com</div>
    </div>

    <div class="hero" role="img" aria-label="Rock waterfall pool with a flower planter and round spa"></div>
    <div class="motto">Every Wave<br>Stays Bright</div>

    <div class="divider divider-blue"></div>
    <div class="divider divider-green"></div>

    <svg class="cover-base" width="600" height="275" viewBox="0 0 600 275" aria-hidden="true">
      <rect width="600" height="275" fill="var(--blue)"/>
      <polygon points="0,0 600,0 600,150 0,182" fill="var(--ice)"/>
      <polygon points="300,182 600,150 600,185" fill="var(--navy)"/>
    </svg>
    <div class="brand"><span class="brand-dot"></span><span class="brand-name">tidewellaqua</span></div>
    <div class="site">tidewellaqua.com</div>

    <div class="social" style="left:41px;top:780px">
      <div class="social-row"><span class="social-mark"></span>www.chatterbook/tidewellaqua</div>
      <div class="social-row"><span class="social-mark alt"></span>circle.searchly.com/+Tidewellaqua</div>
    </div>
  </section>

  <section class="panel panel-about" role="img" aria-label="Dusk sky over desert hills and a blue pool">
    <div class="about">
      <div class="heading">About Us</div>
      <p>A native to Phoenix, Darren Whitcombe founded Tidewell Aqua Service in 2000. Our company was built from the ground up by way of hard work, word of mouth, and determination. Our company will always remain firmly grounded, and continue to develop systems that put our customers first!</p>
      <p>Our philosophy is to treat every pool as if it were our own, run an efficient and organized business, and care for our employees.</p>
      <p>Tidewell Aqua Service is a yearly, proud contributor to the Saguaro Youth Medical Center Splash Smart Day. Please educate and watch all children around water... every accident can be avoided.</p>
    </div>
  </section>

</main>
</body>
</html>
```